letterhead design

We have a business card with logo, ink etc and want to develop letterhead that uses the elements of the business card logo.
Must haves...and they should be designed in, not just plopped in :)
Dr. Marla Quint
2817 W Birch Avenue
Fresno, CA 93728
559-555-0137 p
559-555-0182 f
info@ridgemoorchiropractic.com
www.ridgemoorchiropractic.com
www.friendpage.net/ridgemoorchiro
Updates

Rather than just have the logo on the page, is there someway to silkscreen it in the background to fill the page?

Reason: I was out of town for a week.

Industry/Entity Type

Business

Requirements
Nice to have
• I'd like the logo somehow silk screened in the background of the paper as well.

```html
<!DOCTYPE html>
<html lang="en">
<head>
<meta charset="utf-8">
<title>Ridgemoor Chiropractic Letterhead</title>
<link rel="stylesheet" href="https://fonts.googleapis.com/css2?family=Arimo:wght@400;700&display=swap">
<style>
  :root {
    --mat: #2a2a2a;
    --paper: #ffffff;
    --ink: #1f1f1f;
    --rule-dark: #3a3a3a;
    --rule-light: #e6e6e6;
    --ghost: #ececec;
  }
  * { margin: 0; padding: 0; box-sizing: border-box; }
  html, body {
    width: 914px; height: 1200px; overflow: hidden;
    background: var(--mat);
    font-family: "Arimo", Arial, sans-serif;
    color: var(--ink);
  }
  .sheet {
    position: absolute; left: 90px; top: 90px;
    width: 724px; height: 1021px;
    background: var(--paper);
  }
  .rule {
    position: absolute; left: 0; width: 100%;
    background: linear-gradient(90deg, var(--rule-dark) 0%, var(--rule-light) 45%, var(--rule-light) 55%, var(--rule-dark) 100%);
  }
  .rule--top { top: 3px; height: 4px; }
  .rule--header { top: 87px; height: 3px; }
  .rule--footer {
    top: 990px; height: 2px;
    background: linear-gradient(90deg, var(--rule-dark) 0%, var(--rule-dark) 55%, var(--rule-light) 100%);
  }
  .brand {
    position: absolute; left: 280px; top: 34px;
    display: flex; align-items: center; gap: 8px;
    font-weight: 700; font-size: 22px; letter-spacing: 1px;
    color: var(--ink);
  }
  .brand__mark { width: 12px; height: 12px; background: var(--ink); }
  .doctor {
    position: absolute; left: 524px; top: 13px;
    font-size: 15.5px;
  }
  .phones {
    position: absolute; left: 640px; top: 12px;
    font-size: 10.5px; line-height: 12px;
  }
  .address {
    position: absolute; right: 11px; top: 59px;
    text-align: right; font-size: 12.5px; line-height: 14px;
  }
  .address .email { font-size: 11px; }
  .ghost-brand {
    position: absolute; left: 183px; top: 440px;
    width: 356px; height: 160px;
    display: flex; align-items: center; justify-content: center; gap: 14px;
    font-weight: 700; font-size: 46px; letter-spacing: 2px;
    color: var(--ghost);
  }
  .ghost-brand__mark { width: 26px; height: 26px; background: var(--ghost); }
  .footer-links {
    position: absolute; left: 0; width: 100%; top: 996px;
    text-align: center; padding-left: 70px;
    font-size: 15px; word-spacing: 0;
  }
  .footer-links span + span { margin-left: 12px; }
</style>
</head>
<body>
  <main class="sheet">
    <div class="rule rule--top"></div>

    <div class="brand">
      <span class="brand__mark"></span>
      <span class="brand__name">RIDGEMOOR</span>
    </div>

    <div class="doctor">Dr. Marla Quint</div>
    <div class="phones">
      <div>559-555-0137p</div>
      <div>559-555-0182f</div>
    </div>
    <div class="address">
      <div>2817 W Birch Avenue, Fresno, CA 93728</div>
      <div class="email">info@ridgemoorchiropractic.com</div>
    </div>

    <div class="rule rule--header"></div>

    <div class="ghost-brand" aria-hidden="true">
      <span class="ghost-brand__mark"></span>
      <span>RIDGEMOOR</span>
    </div>

    <div class="rule rule--footer"></div>
    <div class="footer-links">
      <span>www.ridgemoorchiropractic.com</span>
      <span>www.friendpage.net/ridgemoorchiro</span>
    </div>
  </main>
</body>
</html>
```